Unique business card design

Boutique coastal hotel suites - in need of clever stand out business card I have uploaded the logo that I had created through quill forge I want something that is clever and stands out from everyone else - 418 Brantwell Avenue seldovia Alaska 99571 phone or text 907 -581-6142 www.primemarrowbysuites.com

Target Market(s)

Men and woman

Industry/Entity Type

Boutique coastal hotel

Contact Information for Business Card

Marrowby Suites Seldovia Alaska marrowby_suites@mailnest.net

Requirements
Must have
• Classy - clever -bold 907-581-6142 call or text

```html
<!DOCTYPE html>
<html lang="en">
<head>
<meta charset="utf-8">
<title>Marrowby Suites – Business Card</title>
<link href="https://fonts.googleapis.com/css2?family=Montserrat:wght@400;500;600;700&display=swap" rel="stylesheet">
<style>
  :root {
    --backdrop: #e9e5df;
    --card: #141414;
    --navy: #2e5275;
    --navy-band: #355b7e;
    --red: #d03a2f;
    --white: #ffffff;
    --soft-white: #e8e8e8;
  }
  * { margin: 0; padding: 0; box-sizing: border-box; }
  html, body { width: 900px; height: 1200px; overflow: hidden; }
  body {
    background: var(--backdrop);
    font-family: "Montserrat", sans-serif;
    position: relative;
  }
  .card {
    position: absolute;
    left: 80px;
    width: 740px;
    height: 438px;
    background: var(--card);
    border-radius: 30px;
    overflow: hidden;
    box-shadow: 0 6px 14px rgba(0,0,0,0.35);
  }
  .card--front { top: 132px; }
  .card--back { top: 640px; }

  .wordmark {
    position: absolute;
    left: 0; right: 0;
    text-align: center;
    color: var(--navy);
    font-weight: 700;
    letter-spacing: 4px;
    white-space: nowrap;
  }
  .card--front .wordmark { top: 135px; font-size: 50px; }
  .card--back .wordmark { top: 200px; font-size: 54px; }

  .call-band {
    position: absolute;
    top: 245px; left: 0; right: 0;
    height: 41px;
    background: var(--navy-band);
    color: var(--white);
    font-size: 18px;
    display: flex;
    align-items: center;
    justify-content: center;
    gap: 10px;
  }
  .call-band strong { font-weight: 700; }

  .contact-row {
    position: absolute;
    top: 315px; left: 0; right: 0;
    display: flex;
    justify-content: center;
  }
  .person {
    text-align: right;
    padding-right: 18px;
    border-right: 1px solid var(--navy);
  }
  .person__name {
    color: var(--navy);
    font-weight: 700;
    font-size: 25px;
    line-height: 1.1;
  }
  .person__role {
    color: var(--soft-white);
    font-size: 16px;
    margin-top: 4px;
  }
  .links {
    padding-left: 14px;
    color: var(--soft-white);
    font-size: 16px;
    display: flex;
    flex-direction: column;
    gap: 5px;
    padding-top: 2px;
  }
  .links__item { display: flex; align-items: center; gap: 10px; }
  .links__item svg { width: 14px; height: 14px; fill: var(--navy); flex: none; }

  .address-band {
    position: absolute;
    bottom: 0; left: 0; right: 0;
    height: 47px;
    background: var(--navy-band);
    color: var(--soft-white);
    font-size: 16px;
    display: flex;
    align-items: center;
    justify-content: center;
    gap: 12px;
  }
  .address-band svg { width: 12px; height: 15px; fill: var(--white); }

  .back-url {
    position: absolute;
    top: 368px; left: 0; right: 0;
    text-align: center;
    color: var(--white);
    font-size: 15px;
  }
  .back-url span { color: var(--red); }
</style>
</head>
<body>
  <section class="card card--front" aria-label="Business card front">
    <div class="wordmark">MARROWBY SUITES</div>

    <div class="call-band">Phone us Or text Now <strong>555 -581-6142</strong></div>

    <div class="contact-row">
      <div class="person">
        <div class="person__name">Renata Vallance</div>
        <div class="person__role">Managing Director</div>
      </div>
      <div class="links">
        <div class="links__item">
          <svg viewBox="0 0 14 14" aria-hidden="true"><path d="M1 3h12v8H1z"/><path d="M1 3l6 4 6-4v-.5H1z" fill="#1c3550"/></svg>
          nfo@primemarrowbysuites.com
        </div>
        <div class="links__item">
          <svg viewBox="0 0 14 14" aria-hidden="true"><circle cx="7" cy="7" r="6.5"/><path d="M4 4.5c1 .3 1.5 1.2 1 2.2-.4.8.3 1.5 1 1.8.6.3.4 1.5 0 2.5M9 2.5c-.4 1 .4 1.6 1.3 1.8.8.2 1 1.2.5 1.8" stroke="#141414" stroke-width="1" fill="none"/></svg>
          www.primemarrowbysuites.com
        </div>
      </div>
    </div>

    <div class="address-band">
      <svg viewBox="0 0 12 15" aria-hidden="true"><path d="M6 0a6 6 0 0 0-6 6c0 4.5 6 9 6 9s6-4.5 6-9a6 6 0 0 0-6-6zm0 8.3A2.3 2.3 0 1 1 6 3.7a2.3 2.3 0 0 1 0 4.6z"/></svg>
      418 Brantwell Avenue, Harrowick, ME 99571
    </div>
  </section>

  <section class="card card--back" aria-label="Business card back">
    <div class="wordmark">MARROWBY SUITES</div>
    <div class="back-url">www.<span>primemarrowbysuites</span>.com</div>
  </section>
</body>
</html>
```